Book Cover: The Quiet Lantern Keeper

DO NOT JUST COPY THE BOOK COVER I HAVE ADDED FOR REFERENCE. I NEED SOMETHING FRESH NOT JUST A COPY AND PASTE!
If you cannot improve on the design with something creative then don't submit a design.

Project Title:
Book Cover Design for The Quiet Lantern Keeper

Must be better than the mock design I have uploaded in project files.

Project Description:
I’m looking for a striking and emotionally evocative book cover for my upcoming title The Quiet Lantern Keeper. This is a deeply personal and powerful memoir about the masks we wear, emotional survival, control, and the journey toward radical self-awareness and healing. The cover should visually represent the contrast between the performative self and the authentic self.

Visual Concept:
Please take visual inspiration and design continuity from my previous book Rise Past Dusk! — I will upload that cover for reference. This new design should feel like a continuation of the same author journey, but bolder and more psychologically intense.

You’ll be provided with two photos of me:

One where I appear more unkept, raw, and emotionally heavy.

One where I appear clean, centered, and lighter.

These can either be:

Split down the middle to create a “mirror” or duality effect (symbolizing the split self),

Or placed side by side as a subtle before/after or internal/external representation.

You may also consider overlaying or fading one into the other if done tastefully.

The mood should hint at internal conflict, self-reckoning, and healing—but without looking too “self-help cliché.” Think masculine, introspective, modern, and editorial. Avoid overly bright or busy visuals. A minimal or clean design with strong type hierarchy is preferred.

Key Themes to Represent Visually (even abstractly):

Narcissism as a survival mechanism

The emotional cost of performance

The tension between image and authenticity

The healing journey from ego to empathy

Design References:

Rise Past Dusk! (uploaded) — continuity of brand and typography encouraged

Memoir-style covers like Every Harbor Has a Lighthouse, Driftwood, or A River Remembers Stones for layout feel

If using color, muted tones with contrast (black/white, sepia, desaturated blues or greys) work well

Title: The Quiet Lantern Keeper
Subtitle (optional placement): Not every narcissist is a monster. Some are just wounded men trying their best to survive
Author: Marek Tollan

Deliverables:

Full front cover for print sale size as previous cover, including space for subtitle and author name

Spine and back cover (leave placeholder text if no blurb is given)

Ebook cover version

High-resolution files suitable for Pellora PrintHub and print use

Additional Notes:
Please ensure the tone stays emotionally resonant, masculine, and sophisticated. No stock image models or cliché therapist symbols. Use my uploaded photos only.

Looking forward to seeing your vision come to life.

Back Cover Blurb – The Quiet Lantern Keeper
A brutally honest recovery story—about what happens after you get clean, and the ego you still have to face.
Most people think addiction ends when you put down the drink, the drug, or the chaos.
But for Marek Tollan, sobriety was just the start.
Behind the personal development posts, six-pack selfies, and billion-rand property deals, he was still chasing the one thing rehab never took from him: the need to be admired.
This book is not a confession. It’s a dismantling.
In The Quiet Lantern Keeper, Marek exposes the hidden patterns of ego, control, and validation-seeking that nearly cost him everything—even after he got “better.” With fearless self-inquiry and raw storytelling, he invites readers into his recovery from performance, perfectionism, and power addiction.
Whether you’ve been the narcissist—or you’ve loved one—this book is a mirror. And what you’ll find is not just insight, but a new path forward: one where truth is more powerful than charm, and safety matters more than being impressive.
This isn’t about being perfect.
It’s about being honest.
And finally becoming someone worth trusting—especially by yourself.

Target Market(s)

Any reader wanting to read about narcissism and love

Font styles to use
Sans Serif

Colors
EB3D1F
EC4F4E
F09395
F8D3D4
FCEDEE

Requirements
Must have
• Must be better than the mock design I uploaded.

```html
<!DOCTYPE html>
<html lang="en">
<head>
<meta charset="UTF-8">
<title>The Quiet Lantern Keeper — Marek Tollan</title>
<link rel="stylesheet" href="https://fonts.googleapis.com/css2?family=Bebas+Neue&display=swap">
<style>
  :root {
    --paper: #efeeec;
    --ink: #1b1a1a;
    --red: #c01b17;
    --white: #ffffff;
    --divider: #3a1414;
  }
  * { margin: 0; padding: 0; box-sizing: border-box; }
  html, body { width: 846px; height: 1200px; overflow: hidden; background: var(--paper); }
  .cover {
    position: relative;
    width: 846px;
    height: 1200px;
    overflow: hidden;
    background: radial-gradient(ellipse at 50% 40%, #f5f4f2 0%, var(--paper) 70%);
    font-family: "Bebas Neue", "Oswald", sans-serif;
  }
  .portrait {
    position: absolute;
    left: 176px; top: 360px;
    width: 520px; height: 840px;
    z-index: 1;
  }
  .title-tab {
    position: absolute;
    left: 68px; top: 0;
    width: 73px; height: 194px;
    background: var(--red);
    z-index: 2;
  }
  .title-tab__word {
    position: absolute;
    left: 50%; bottom: 4px;
    transform: translateX(-50%) rotate(-90deg);
    color: var(--white);
    font-size: 64px;
    line-height: 1;
    width: 82px;
    text-align: center;
    margin-bottom: 10px;
  }
  .title-top {
    position: absolute;
    left: 151px; top: 98px;
    font-size: 116px;
    font-weight: 400;
    line-height: 1;
    color: var(--ink);
    white-space: nowrap;
    letter-spacing: 1px;
    z-index: 2;
  }
  .title-rule {
    position: absolute;
    left: 68px; right: 0; top: 214px;
    height: 5px;
    background: var(--red);
    z-index: 2;
  }
  .title-main {
    position: absolute;
    left: 64px; top: 226px;
    font-size: 214px;
    line-height: 1;
    color: var(--red);
    white-space: nowrap;
    letter-spacing: 4px;
    z-index: 3;
  }
  .subtitle {
    position: absolute;
    left: 68px; top: 408px;
    font-size: 30px;
    line-height: 31px;
    color: var(--ink);
    z-index: 3;
  }
  .subtitle .accent { color: var(--red); }
  .subtitle .accent--large { font-size: 36px; }
  .author {
    position: absolute;
    left: 746px; top: 942px;
    transform: translate(-50%, -50%) rotate(-90deg);
    font-size: 84px;
    line-height: 1;
    color: var(--ink);
    white-space: nowrap;
    letter-spacing: 2px;
    z-index: 3;
  }
</style>
</head>
<body>
<main class="cover">
  <svg class="portrait" viewBox="0 0 520 840" role="img" aria-label="Split portrait of the author: left half raw and bearded in dark desaturated sepia, right half clean-shaven and smiling in warm natural colour">
    <defs>
      <linearGradient id="raw-half" x1="0" y1="0" x2="0" y2="1">
        <stop offset="0" stop-color="#3b2826"/>
        <stop offset="0.45" stop-color="#7a6a66"/>
        <stop offset="0.8" stop-color="#4a3634"/>
        <stop offset="1" stop-color="#261a1a"/>
      </linearGradient>
      <linearGradient id="clean-half" x1="0" y1="0" x2="0" y2="1">
        <stop offset="0" stop-color="#3a2e2a"/>
        <stop offset="0.3" stop-color="#d9a996"/>
        <stop offset="0.7" stop-color="#d69684"/>
        <stop offset="1" stop-color="#e9d8d0"/>
      </linearGradient>
    </defs>
    <path d="M260 0 C140 0 70 110 70 260 C70 330 30 380 50 520 C70 600 0 700 0 840 L260 840 Z" fill="url(#raw-half)"/>
    <path d="M260 0 C380 0 450 110 450 260 C450 330 490 380 470 520 C450 600 520 700 520 840 L260 840 Z" fill="url(#clean-half)"/>
    <rect x="255" y="0" width="11" height="840" fill="var(--divider)"/>
  </svg>

  <div class="title-tab"><span class="title-tab__word">THE</span></div>
  <h1 class="title-top">QUIET LANTERN</h1>
  <div class="title-rule"></div>
  <div class="title-main">KEEPER</div>

  <p class="subtitle">
    NOT EVERY<br>
    <span class="accent accent--large">NARCISSIST</span><br>
    IS A MONSTER.<br>
    SOME ARE<br>
    <span class="accent">JUST WOUNDED</span><br>
    MEN TRYING<br>
    THEIR BEST TO<br>
    <span class="accent">SURVIVE</span>
  </p>

  <div class="author">MAREK TOLLAN</div>
</main>
</body>
</html>
```